International Dating Community Needs a Web Design

We need a single page web design built on plomet.com. Designers need to design a one page web design on PLOMET, take a screenshot and paste it here. Once the winner is chosen, the designer needs to give me access to the design and transfer over the implementation.
REQUIREMENTS:
- Designer MUST design on plomet.com (http://www.plomet.com/support/main/html5/getting-started/signing-free)
- Once designed, designer needs to take a screenshot of the plomet design and submit the design on artvessel.
- Please add the site url as the design comment when you submit the design
- Any designers that use existing PLOMET templates will NOT be eligible to win and will be eliminated.
Note: If you use any stock images, simply let me know the numbers and I will purchase them.
PAGE INFORMATION:
Color Scheme:
- Light Blue / Cyan
- White
- Black / Dark Gray
Header:
- Logo (attached) on the left
- Login / Register on the right
Navigation bar:
- Home
- Events
- Entertainment / Music
- Gallery
- Membership
- About Us
Homepage Content:
The worlds #1 destination for international dating!
We may be new to you, but our team have been around for longer than you think. We're here to promote upcoming cultural events in your community, promote local businesses serving your community & soon we will also be offering an online dating service to meet others within the area.
If you're interested in learning more about events & concerts relating to the community then make sure you like us on Chatterbox.
If you have any comments or feedback, we'd love to hear from you! Click here to contact us.
Photos:
Im open for you to use any photos you like - some sites I like:
http://www.openpicturebank.net/images/People_g40.html
http://www.qvr.hu/category/135

```html
<!DOCTYPE html>
<html lang="en">
<head>
<meta charset="utf-8">
<title>Tandara – International Dating Community</title>
<link href="https://fonts.googleapis.com/css2?family=Open+Sans:wght@400;600;700&family=Arimo:wght@400;700&family=Kaushan+Script&display=swap" rel="stylesheet">
<style>
  :root {
    --teal: #35b6a5;
    --mint: #d3ece8;
    --white: #ffffff;
    --orange: #f6891f;
    --grey: #9a9a9a;
    --dark-grey: #6b6b6b;
    --icon-grey: #777777;
    --blue: #0d7ec4;
    --ink: #333333;
  }
  * { box-sizing: border-box; margin: 0; padding: 0; }
  html, body { width: 947px; height: 1200px; overflow: hidden; background: var(--white); }
  body { position: relative; font-family: "Open Sans", Arial, sans-serif; }

  .hero { position: absolute; left: 0; top: 0; width: 947px; height: 372px; background: var(--teal); }
  .brand { position: absolute; left: 100px; top: 0; font-family: "Open Sans", sans-serif; font-size: 26px; font-weight: 400; color: var(--white); letter-spacing: 1px; line-height: 28px; }
  .main-nav { position: absolute; top: 8px; left: 0; font-family: "Arimo", Arial, sans-serif; font-size: 11px; font-weight: 700; }
  .main-nav a { position: absolute; color: var(--white); text-decoration: none; white-space: nowrap; }
  .account { position: absolute; top: 3px; font-family: "Arimo", Arial, sans-serif; font-size: 12px; }
  .account a { position: absolute; top: 0; height: 22px; line-height: 22px; background: var(--white); color: var(--ink); text-decoration: none; text-align: center; border-radius: 3px; }
  .hero-title { position: absolute; left: 0; width: 880px; top: 112px; text-align: center; color: var(--white); font-size: 29px; line-height: 38px; }
  .hero-title strong { display: block; font-weight: 700; }
  .hero-title span { display: block; font-weight: 400; }
  .hero-art { position: absolute; left: 294px; top: 268px; width: 306px; height: 104px; background: var(--white); border-radius: 153px 153px 0 0 / 104px 104px 0 0; }

  .intro { position: absolute; left: 0; top: 372px; width: 947px; height: 402px; background: var(--white); }
  .intro-lead { position: absolute; left: 0; width: 947px; top: 40px; text-align: center; font-size: 19px; line-height: 20px; color: var(--grey); }
  .intro-lead em { font-style: normal; color: var(--orange); }

  .service { position: absolute; text-align: center; font-family: "Arimo", Arial, sans-serif; font-weight: 700; color: var(--dark-grey); }
  .service-icon { position: absolute; background: var(--icon-grey); border-radius: 8px; opacity: .85; }
  .service-script { position: absolute; left: 0; right: 0; font-family: "Kaushan Script", cursive; font-weight: 400; font-size: 27px; color: var(--orange); transform: rotate(-6deg); }
  .service-label { position: absolute; left: 0; right: 0; }

  .social { position: absolute; left: 0; top: 774px; width: 947px; height: 278px; background: var(--mint); }
  .social-notch { position: absolute; left: 458px; top: -1px; }
  .social-text { position: absolute; left: 88px; top: 96px; width: 335px; font-size: 19px; line-height: 21px; color: var(--grey); }
  .social-text em { font-style: normal; color: var(--orange); }
  .social-badge { position: absolute; left: 560px; top: 50px; }

  .feedback { position: absolute; left: 0; top: 1052px; width: 947px; height: 116px; background: var(--teal); text-align: center; }
  .feedback p { position: absolute; left: 0; width: 947px; top: 25px; font-size: 15px; font-weight: 600; color: var(--white); }
  .contact-button { position: absolute; left: 390px; top: 57px; width: 166px; height: 23px; line-height: 23px; background: var(--white); color: var(--ink); border-radius: 3px; font-family: "Arimo", Arial, sans-serif; font-size: 12px; text-decoration: none; }

  .site-footer { position: absolute; left: 0; top: 1168px; width: 947px; height: 32px; text-align: center; font-family: "Arimo", Arial, sans-serif; font-size: 10px; line-height: 32px; color: var(--ink); }
</style>
</head>
<body>
  <header class="hero">
    <div class="brand">tandara</div>
    <nav class="main-nav">
      <a href="#" style="left:295px">Home</a>
      <a href="#" style="left:347px">Events</a>
      <a href="#" style="left:404px">Gallery</a>
      <a href="#" style="left:462px">Membership</a>
      <a href="#" style="left:542px">About Us</a>
    </nav>
    <div class="account">
      <a href="#" style="left:697px;width:67px">Login</a>
      <a href="#" style="left:778px;width:68px">Register</a>
    </div>
    <h1 class="hero-title"><strong>The worlds #1 destination</strong><span>for international dating!</span></h1>
    <div class="hero-art" role="img" aria-label="Illustration of a white globe surrounded by floating orange and white hearts"></div>
  </header>

  <section class="intro">
    <p class="intro-lead">We may be new to you,<br>but our team have been around for longer<br>than you think. <em>We are here to...</em></p>

    <div class="service" style="left:110px;top:194px;width:174px;height:150px">
      <div class="service-icon" role="img" aria-label="Music note icon" style="left:26px;top:0;width:92px;height:100px"></div>
      <div class="service-script" style="top:82px">Promote</div>
      <div class="service-label" style="top:128px;font-size:15px">Cultural Events</div>
    </div>

    <div class="service" style="left:385px;top:179px;width:154px;height:160px">
      <div class="service-icon" role="img" aria-label="Office building icon" style="left:36px;top:0;width:85px;height:109px"></div>
      <div class="service-script" style="top:100px">Promote</div>
      <div class="service-label" style="top:149px;font-size:12px">Local businesses</div>
    </div>

    <div class="service" style="left:622px;top:160px;width:210px;height:200px">
      <div class="service-icon" role="img" aria-label="Icon of a man and a woman with speech bubbles and a star" style="left:46px;top:0;width:112px;height:128px"></div>
      <div class="service-script" style="top:122px">And Soon,</div>
      <div class="service-label" style="top:168px;font-size:12px;line-height:15px">We will also be offering an<br>online dating service.</div>
    </div>
  </section>

  <section class="social">
    <svg class="social-notch" width="31" height="20" viewBox="0 0 31 20" aria-hidden="true"><polygon points="0,0 31,0 15.5,20" fill="#ffffff"/></svg>
    <p class="social-text"><em>If you're interested in learning more about events &amp; concerts</em> relating to the community then make sure you like us on Chatterbox.</p>
    <svg class="social-badge" width="260" height="200" viewBox="0 0 260 200" aria-label="Like us on Chatterbox">
      <circle cx="97" cy="48" r="30" fill="#ffffff"/>
      <circle cx="180" cy="42" r="30" fill="#35b6a5"/>
      <circle cx="43" cy="132" r="28" fill="#35b6a5"/>
      <circle cx="150" cy="160" r="34" fill="#35b6a5"/>
      <circle cx="88" cy="96" r="76" fill="#0d7ec4"/>
      <text x="68" y="101" text-anchor="middle" font-family="Open Sans, sans-serif" font-size="14" font-weight="700" fill="#ffffff">Chatterbox</text>
      <circle cx="182" cy="104" r="54" fill="#f6891f"/>
      <text x="182" y="117" text-anchor="middle" font-family="Arimo, Arial, sans-serif" font-size="36" font-weight="700" fill="#ffffff">GO</text>
    </svg>
  </section>

  <section class="feedback">
    <p>If you have any comments or feedback, we'd love to hear from you!</p>
    <a class="contact-button" href="#">Click here to contact us</a>
  </section>

  <footer class="site-footer">© Tandara. 2014 All Rights Reserved.</footer>
</body>
</html>
```